New Year's Eve Wedding Save the Date

Mira and Kevin (we) are getting married 2016-12-31. I'm a hockey player, and she's into movies... we have 2 yellow labs, and we want a Save the Date postcard that matches our personality and the excitement of the event. See attached mock up that I've created (which will be what we fall back on if we can't find a design we like). I like the idea of the silhouette people and dogs under fireworks but am open to other concepts as well. String lights, champagne bottles/flutes, etc...

Industry/Entity Type

Wedding

Font styles to use
Script

```html
<!DOCTYPE html>
<html lang="en">
<head>
<meta charset="utf-8">
<title>Save the Date – Kevin &amp; Mira</title>
<link rel="stylesheet" href="https://fonts.googleapis.com/css2?family=Cinzel:wght@400;600;700&family=Great+Vibes&family=Cormorant+Garamond:ital,wght@1,500;1,700&display=swap">
<style>
  :root {
    --page-bg: #e6e6e4;
    --card-edge: #3a3f43;
    --gold: #c4a261;
    --paper: #f4f0e6;
    --ink: #1d1d1d;
    --rule: #b9b5ab;
    --white: #ffffff;
    --sky-top: #141326;
    --sky-mid: #2e2542;
    --glow: #8a4a2e;
    --spark: #e9a66a;
  }
  * { box-sizing: border-box; margin: 0; padding: 0; }
  html, body { width: 1200px; height: 1200px; overflow: hidden; }
  body {
    background: var(--page-bg);
    display: flex; flex-direction: column; align-items: center; justify-content: center;
    gap: 40px;
  }
  .postcard {
    position: relative; width: 780px; height: 520px;
    background: var(--card-edge);
  }
  .postcard__frame {
    position: absolute; inset: 18px;
    border: 10px solid var(--gold);
    overflow: hidden;
  }
  .postcard__perforation { position: absolute; inset: 0; pointer-events: none; }
  .postcard__notch {
    position: absolute; top: 50%; width: 84px; height: 84px; margin-top: -42px;
    border-radius: 50%; background: var(--card-edge);
    border: 10px solid var(--gold); z-index: 2;
  }
  .postcard__notch--left { left: -24px; }
  .postcard__notch--right { right: -24px; }

  /* Front */
  .front__scene {
    position: absolute; inset: 0;
    background:
      radial-gradient(ellipse 30% 35% at 78% 78%, var(--spark) 0%, rgba(233,166,106,0.35) 35%, transparent 70%),
      radial-gradient(ellipse 20% 25% at 92% 60%, rgba(233,166,106,0.7) 0%, transparent 70%),
      radial-gradient(ellipse 60% 30% at 45% 95%, var(--glow) 0%, transparent 70%),
      linear-gradient(180deg, var(--sky-top) 0%, var(--sky-mid) 60%, #3a2330 100%);
  }
  .front__silhouettes {
    position: absolute; left: 30px; bottom: 0; width: 290px; height: 230px;
    background: linear-gradient(90deg, rgba(205,205,210,0.55), rgba(40,40,45,0.85));
    border-radius: 40% 40% 0 0;
  }
  .front__title {
    position: absolute; left: 250px; top: 36px; width: 420px;
    color: var(--white); text-align: center; font-family: "Cinzel", serif;
  }
  .front__kicker {
    font-size: 40px; letter-spacing: 1px; line-height: 1;
    border-bottom: 2px solid var(--white); padding-bottom: 8px; margin: 0 20px;
  }
  .front__names { font-size: 62px; line-height: 1.05; margin-top: 8px; font-weight: 600; }
  .front__amp { font-family: "Great Vibes", cursive; font-weight: 400; font-size: 66px; }
  .front__date { font-size: 42px; font-weight: 700; line-height: 1; }
  .front__year {
    display: inline-block; margin-top: 10px; font-size: 14px; letter-spacing: 1px;
    border-top: 1px solid var(--white); border-bottom: 1px solid var(--white); padding: 3px 10px;
  }
  .front__quote {
    position: absolute; left: 60px; bottom: 6px;
    font-family: "Cormorant Garamond", serif; font-style: italic; font-size: 14px;
    color: var(--white);
  }

  /* Back */
  .back .postcard__frame { background: var(--paper); }
  .back__badge {
    position: absolute; left: 70px; top: 26px; width: 190px; height: 190px;
    border-radius: 50%; background: var(--ink); color: var(--white);
    font-family: "Cinzel", serif; text-align: center;
    display: flex; flex-direction: column; align-items: center; justify-content: center;
  }
  .back__badge-kicker { font-size: 17px; }
  .back__badge-names { font-size: 28px; font-weight: 600; line-height: 1.05; }
  .back__badge-amp { font-family: "Great Vibes", cursive; font-weight: 400; }
  .back__badge-date { font-size: 19px; font-weight: 700; }
  .back__badge-year { font-size: 8px; margin-top: 4px; border-top: 1px solid var(--white); padding-top: 2px; }
  .back__deliver {
    position: absolute; left: 420px; top: 44px;
    font-family: "Cormorant Garamond", serif; font-style: italic; font-weight: 700; font-size: 17px;
    color: var(--ink);
  }
  .back__lines { position: absolute; left: 410px; top: 110px; width: 270px; }
  .back__line { height: 1px; background: var(--rule); margin-bottom: 46px; }
  .back__stamp {
    position: absolute; right: 40px; top: 22px; width: 54px; height: 60px;
    border: 1.5px solid var(--rule);
    font-family: "Great Vibes", cursive; font-size: 16px; color: var(--ink);
    display: flex; align-items: center; justify-content: center;
  }
  .back__follow {
    position: absolute; left: 70px; bottom: 30px;
    font-family: "Cormorant Garamond", serif; font-style: italic; font-weight: 700; font-size: 17px;
    color: var(--ink);
  }
</style>
</head>
<body>

  <section class="postcard front">
    <div class="postcard__frame">
      <div class="front__scene" role="img" aria-label="Night sky photograph with fireworks over a glowing valley, trees and city lights"></div>
      <div class="front__silhouettes" role="img" aria-label="Silhouettes of a bride, a groom and two dogs"></div>
      <div class="front__title">
        <p class="front__kicker">Save the Date</p>
        <p class="front__names">KEVIN <span class="front__amp">&amp;</span> MIRA</p>
        <p class="front__date">DECEMBER 31ST</p>
        <p class="front__year">TWO THOUSAND AND SIXTEEN</p>
      </div>
      <p class="front__quote">Love is when the other person's happiness is more important than your own</p>
    </div>
    <span class="postcard__notch postcard__notch--left"></span>
    <span class="postcard__notch postcard__notch--right"></span>
  </section>

  <section class="postcard back">
    <div class="postcard__frame">
      <div class="back__badge">
        <p class="back__badge-kicker">SAVE THE DATE</p>
        <p class="back__badge-names">KEVIN<span class="back__badge-amp">&amp;</span>MIRA</p>
        <p class="back__badge-date">DECEMBER 31ST</p>
        <p class="back__badge-year">TWO THOUSAND AND SIXTEEN</p>
      </div>
      <p class="back__deliver">Please deliver to:</p>
      <div class="back__lines">
        <div class="back__line"></div>
        <div class="back__line"></div>
        <div class="back__line"></div>
        <div class="back__line"></div>
      </div>
      <div class="back__stamp">Stamp</div>
      <p class="back__follow">Formal invitation to follow</p>
    </div>
    <span class="postcard__notch postcard__notch--left"></span>
    <span class="postcard__notch postcard__notch--right"></span>
  </section>

</body>
</html>
```